Tending Our Garden eBook Cover Design

I want to deisgn a cover for my eBook (FRONT COVER) and the title is:

UNDER THE WILLOW TREE; WHERE I FOUND MY QUIET STRENGTH AND WHERE YOU MIGHT TOO
By KT Dorran

TITLE CHANGED TO: UNDER THE WILLOW TREE; WHERE I FOUND MY QUIET STRENGTH AND WHERE YOU MIGHT TOO

The color palette is attached. Along with some photos options of me. Along with the ebook in WORD Document. My website is www.KTDorranLive.example. You can use a different color palette if you think it is best

Target Market(s)

women who look to build a personal brand

Industry/Entity Type

health and wellness

Requirements
Must have
• the title
Nice to have
• use my picture on the cover; but that is optional
Should not have
• any men

```html
<!DOCTYPE html>
<html lang="en">
<head>
<meta charset="utf-8">
<title>Under the Willow Tree – eBook Cover</title>
<link rel="stylesheet" href="https://fonts.googleapis.com/css2?family=Barlow:wght@500&family=Barlow+Condensed:wght@500&display=swap">
<style>
  :root {
    --page: #ffffff;
    --cover: #000000;
    --ink-light: #ffffff;
    --gold-deep: #a97a26;
    --gold-mid: #d4a94a;
    --gold-bright: #f6d886;
  }
  html, body {
    margin: 0;
    padding: 0;
    width: 1200px;
    height: 901px;
    overflow: hidden;
    background: var(--page);
  }
  .canvas {
    position: relative;
    width: 1200px;
    height: 901px;
  }
  .cover {
    position: absolute;
    display: block;
  }
  .cover--large { left: 0; top: 0; width: 610px; height: 901px; }
  .cover--small { left: 721px; top: 166px; width: 389px; height: 582px; }
  .cover-bg { fill: var(--cover); }
  .kicker, .subtitle, .byline {
    font-family: "Barlow", Arial, sans-serif;
    font-weight: 500;
    fill: var(--ink-light);
    text-anchor: middle;
  }
  .kicker { font-size: 20px; letter-spacing: 4px; }
  .subtitle { font-size: 18px; letter-spacing: 3px; }
  .byline { font-size: 21px; letter-spacing: 4px; }
  .headline {
    font-family: "Barlow Condensed", "Arial Narrow", sans-serif;
    font-weight: 500;
    font-size: 156px;
  }
  .gold-stop-1 { stop-color: var(--gold-deep); }
  .gold-stop-2 { stop-color: var(--gold-bright); }
  .gold-stop-3 { stop-color: var(--gold-mid); }
  .gold-stop-4 { stop-color: var(--gold-bright); }
</style>
</head>
<body>
<main class="canvas">
  <svg class="cover cover--large" viewBox="0 0 610 901" xmlns="http://www.w3.org/2000/svg" aria-label="eBook front cover">
    <defs>
      <linearGradient id="gold" x1="0" y1="0" x2="1" y2="1">
        <stop class="gold-stop-1" offset="0"/>
        <stop class="gold-stop-2" offset="0.35"/>
        <stop class="gold-stop-3" offset="0.65"/>
        <stop class="gold-stop-4" offset="1"/>
      </linearGradient>
      <symbol id="cover-art" viewBox="0 0 610 901">
        <rect class="cover-bg" width="610" height="901"/>
        <text class="kicker" x="305" y="141">UNDER THE WILLOW TREE;</text>
        <g class="headline" fill="url(#gold)">
          <text x="85" y="275" textLength="451" lengthAdjust="spacingAndGlyphs">WHERE I</text>
          <text x="85" y="400" textLength="451" lengthAdjust="spacingAndGlyphs">FOUND MY</text>
          <text x="85" y="557" textLength="178" lengthAdjust="spacingAndGlyphs">QU</text>
          <text x="360" y="557" textLength="176" lengthAdjust="spacingAndGlyphs">ET</text>
        </g>
        <g class="title-rule" fill="url(#gold)">
          <rect x="85" y="421" width="178" height="4"/>
          <rect x="360" y="421" width="176" height="4"/>
        </g>
        <rect class="emblem" x="272" y="410" width="80" height="210" rx="30" fill="url(#gold)"
              role="img" aria-label="Gold emblem of a leafy figure standing in for the letter I"/>
        <text class="subtitle" x="305" y="650">STRENGTH AND WHERE YOU MIGHT TOO</text>
        <text class="byline" x="305" y="865">BY KT DORRAN</text>
      </symbol>
    </defs>
    <use href="#cover-art" width="610" height="901"/>
  </svg>

  <svg class="cover cover--small" viewBox="0 0 610 901" preserveAspectRatio="none" xmlns="http://www.w3.org/2000/svg" aria-label="eBook front cover, thumbnail">
    <use href="#cover-art" width="610" height="901"/>
  </svg>
</main>
</body>
</html>
```